I need a business Card Design for my practice , i am clinical herbalist. I am a herbalist specializing in Lyme disease, autism, autoimmune diseases, difficult to cure diseasesDifficult to cure diseases. In my innovative practice i link traditional medicine, herbs with science, immunologu ,pharmacology.

Industry/Entity Type

Business

Contact Information for Business Card

My company name : OŚRODEK ZIELNIK
My name : Piotr Kaleta
Name of my profession : Fitoterapeuta
In Polish language Fitoterapeuta is Herbalist .

e-mail: piotrkaleta@osrodekzielnik.com
www.osrodek-zielnik.pl
phone : 604 587 231
My company adress : Dąbrowa Sitnicka 41 , 38-415 Zielnikowo
I dont have logo .

Requirements
Nice to have
• My company

```html
<!DOCTYPE html>
<html lang="pl">
<head>
<meta charset="utf-8">
<title>Ośrodek Zielnik – wizytówka</title>
<link rel="stylesheet" href="https://fonts.googleapis.com/css2?family=Ubuntu:wght@400;500&display=swap">
<style>
  :root {
    --backdrop: #ecebe8;
    --card: #ffffff;
    --charcoal: #333333;
    --orange: #f0832a;
    --text-dark: #2e2e2e;
    --text-grey: #5a5a5a;
  }
  * { margin: 0; padding: 0; box-sizing: border-box; }
  html, body {
    width: 1200px; height: 1200px; overflow: hidden;
    background: var(--backdrop);
    font-family: "Ubuntu", sans-serif;
  }
  .business-card {
    position: absolute; left: 100px; top: 315px;
    width: 1000px; height: 570px;
    background: var(--card);
    box-shadow: 0 6px 24px rgba(0,0,0,.12);
    overflow: hidden;
  }
  .card-graphics { position: absolute; inset: 0; }
  .brand {
    position: absolute; right: 60px; top: 70px;
    display: flex; align-items: center; gap: 18px;
    white-space: nowrap;
  }
  .brand-square { width: 38px; height: 38px; background: var(--orange); flex: none; }
  .brand-name {
    font-size: 40px; font-weight: 500; letter-spacing: 3px;
    color: var(--orange);
  }
  .person { position: absolute; left: 172px; top: 178px; }
  .person-name { font-size: 42px; font-weight: 500; color: var(--text-dark); }
  .person-role { font-size: 21px; color: var(--text-grey); margin-top: 6px; }
  .contact-list {
    position: absolute; left: 175px; top: 336px;
    list-style: none; white-space: nowrap;
  }
  .contact-list li {
    height: 38px; line-height: 38px;
    font-size: 21px; color: var(--text-grey);
  }
</style>
</head>
<body>
  <div class="business-card">
    <svg class="card-graphics" width="1000" height="570" viewBox="0 0 1000 570">
      <path class="side-band" fill="var(--charcoal)"
            d="M0 0 H34 V205 C34 225 50 232 70 236 C100 242 115 255 115 285 V570 H0 Z"/>
      <g class="person-icon" fill="var(--orange)">
        <circle cx="62" cy="190" r="9"/>
        <path d="M46 218 C46 204 54 201 62 201 C70 201 78 204 78 218 Z"/>
      </g>
      <g class="contact-bars" fill="var(--orange)">
        <rect x="22" y="340" width="128" height="30"/>
        <rect x="22" y="378" width="128" height="30"/>
        <rect x="22" y="416" width="128" height="30"/>
        <rect x="22" y="454" width="128" height="30"/>
      </g>
      <g class="contact-icons" fill="none" stroke="#fff" stroke-width="2.2" stroke-linecap="round" stroke-linejoin="round">
        <path class="icon-phone" fill="#fff" stroke="none"
              d="M80 345 l5 0 l3 6 l-3 3 c2 4 4 6 8 8 l3 -3 l6 3 l0 5 c-12 1 -23 -10 -22 -22 z"/>
        <g class="icon-globe">
          <circle cx="90" cy="393" r="10"/>
          <path d="M80 393 H100 M90 383 C84 388 84 398 90 403 M90 383 C96 388 96 398 90 403"/>
        </g>
        <g class="icon-mail">
          <rect x="79" y="424" width="22" height="15"/>
          <path d="M79 424 L90 433 L101 424"/>
        </g>
        <path class="icon-pin" fill="#fff" stroke="none"
              d="M90 458 c-5 0 -8 4 -8 8 c0 6 8 14 8 14 c0 0 8 -8 8 -14 c0 -4 -3 -8 -8 -8 z m0 5 a3 3 0 1 1 0 6 a3 3 0 1 1 0 -6 z"/>
      </g>
      <g class="edge-tabs" fill="var(--orange)">
        <rect x="972" y="272" width="28" height="28"/>
        <rect x="972" y="306" width="28" height="28"/>
        <rect x="972" y="340" width="28" height="28"/>
        <rect x="972" y="374" width="28" height="28"/>
      </g>
    </svg>

    <div class="brand">
      <span class="brand-square"></span>
      <span class="brand-name">OŚRODEK ZIELNIK</span>
    </div>

    <div class="person">
      <h1 class="person-name">Piotr Kaleta</h1>
      <p class="person-role">Fitoterapeuta</p>
    </div>

    <ul class="contact-list">
      <li class="contact-phone">604 587 231</li>
      <li class="contact-web">www.osrodek-zielnik.pl</li>
      <li class="contact-mail">piotrkaleta@osrodekzielnik.com</li>
      <li class="contact-address">Dąbrowa Sitnicka 41 , 38-415 Zielnikowo</li>
    </ul>
  </div>
</body>
</html>
```